design an extra page for our profile

we are looking for someone to create another page like the attached but with the below changes:
heading changed to (Construction)
icons changed and names to reflect new services i.e
- Residential Building
- Commercial Building
- Landscaping
- Concrete
- Painting

the very bottom of the page is to stay the same with our office info

```html
<!DOCTYPE html>
<html lang="en">
<head>
<meta charset="utf-8">
<title>Construction – Services</title>
<link href="https://fonts.googleapis.com/css2?family=Poppins:wght@400;500;600;700&display=swap" rel="stylesheet">
<style>
  :root{
    --olive:#77782f;
    --ink:#111111;
    --white:#ffffff;
    --hero-dark:#14262a;
    --hero-mid:#2c4a4c;
    --glow:#d7a24a;
    --sky:#9fcde6;
    --sky-soft:#d6ebf5;
    --glass:#b9d3e2;
    --grass:#c9d27a;
  }
  *{margin:0;padding:0;box-sizing:border-box}
  html,body{width:848px;height:1200px;overflow:hidden;background:var(--white)}
  body{font-family:'Poppins',sans-serif;color:var(--ink)}
  .page{position:relative;width:848px;height:1200px;overflow:hidden;background:var(--white)}

  .hero{position:absolute;left:0;top:0;width:848px;height:328px;
    background:
      radial-gradient(ellipse 220px 140px at 430px 40px, rgba(215,162,74,.85), rgba(215,162,74,0) 70%),
      linear-gradient(115deg, rgba(255,255,255,0) 0 30%, rgba(120,160,160,.18) 30% 46%, rgba(255,255,255,0) 46% 100%),
      linear-gradient(70deg, rgba(255,255,255,0) 0 62%, rgba(90,130,130,.16) 62% 78%, rgba(255,255,255,0) 78% 100%),
      linear-gradient(160deg, var(--hero-mid) 0%, var(--hero-dark) 55%, #0d1a1d 100%);}
  .hero-title{position:absolute;left:178px;top:116px;width:495px;height:94px;
    border:2px solid var(--white);display:flex;align-items:center;justify-content:center;
    color:var(--white);font-weight:600;font-size:52px;letter-spacing:1px;}

  .service{position:absolute;width:220px;text-align:center}
  .service svg{display:block;margin:0 auto;width:100px;height:94px}
  .service-name{margin-top:12px;font-weight:700;font-size:13px;letter-spacing:.3px;text-transform:uppercase}
  .s-residential{left:69px;top:384px}
  .s-landscaping{left:315px;top:384px}
  .s-commercial{left:556px;top:384px}
  .s-concrete{left:202px;top:534px}
  .s-painting{left:422px;top:534px}

  .skyline{position:absolute;left:100px;top:680px;width:700px;height:390px;
    background:
      radial-gradient(ellipse 300px 70px at 50% 96%, var(--grass) 0%, rgba(201,210,122,.7) 55%, rgba(201,210,122,0) 100%),
      radial-gradient(ellipse 260px 200px at 50% 68%, var(--glass) 0%, rgba(159,205,230,.85) 50%, rgba(159,205,230,0) 100%),
      radial-gradient(ellipse 360px 150px at 55% 28%, var(--sky) 0%, var(--sky-soft) 55%, rgba(214,235,245,0) 100%);}

  .footer{position:absolute;left:0;top:1052px;width:848px;height:148px;background:var(--olive);color:var(--white)}
  .brand{position:absolute;left:34px;top:60px;display:flex;align-items:center;gap:8px;
    font-weight:700;font-size:22px;letter-spacing:1px}
  .brand-dot{width:14px;height:14px;border-radius:50%;background:var(--white)}
  .contact{position:absolute;left:160px;top:60px;width:652px;font-size:14.5px;font-weight:500}
  .contact-row{display:flex;justify-content:space-between;align-items:center;height:24px;white-space:nowrap}
  .contact-row strong{font-weight:700}
  .sep{margin:0 14px}
  .contact-rule{height:1px;background:rgba(255,255,255,.8);margin:4px 0 5px}
  .cities{letter-spacing:1px}
</style>
</head>
<body>
<div class="page">
  <header class="hero" role="img" aria-label="Upward view of glass high-rise towers with sunlight bursting between them">
    <h1 class="hero-title">CONSTRUCTION</h1>
  </header>

  <div class="service s-residential">
    <svg viewBox="0 0 100 94" fill="none" stroke="var(--olive)" stroke-width="4" stroke-linejoin="round">
      <path d="M30 50 L56 24 L84 50"/><path d="M36 46 V80 H78 V46"/>
      <rect x="44" y="52" width="12" height="12"/><rect x="62" y="52" width="10" height="28"/>
      <path d="M50 30 V18 H60 V28"/><circle cx="22" cy="58" r="12"/>
      <path d="M6 92 H96 M8 80 H92 M14 80 V92 M26 80 V92 M38 80 V92 M50 80 V92 M62 80 V92 M74 80 V92 M86 80 V92"/>
    </svg>
    <div class="service-name">Residential Building</div>
  </div>

  <div class="service s-landscaping">
    <svg viewBox="0 0 100 94" fill="none" stroke="var(--olive)" stroke-width="4" stroke-linecap="round">
      <circle cx="50" cy="24" r="7"/>
      <circle cx="50" cy="10" r="6"/><circle cx="50" cy="38" r="6"/><circle cx="36" cy="24" r="6"/><circle cx="64" cy="24" r="6"/>
      <path d="M50 44 V78 M50 64 C40 56 34 60 34 66 C42 68 48 66 50 64 M50 58 C60 50 66 54 66 60 C58 62 52 60 50 58"/>
      <path d="M24 88 C30 76 70 76 76 88 M10 88 H90"/>
    </svg>
    <div class="service-name">Landscaping</div>
  </div>

  <div class="service s-commercial">
    <svg viewBox="0 0 100 94" fill="none" stroke="var(--olive)" stroke-width="4">
      <rect x="12" y="8" width="60" height="80"/><path d="M12 18 H72 M72 30 H90 V88 M4 88 H96"/>
      <g fill="var(--olive)" stroke="none">
        <rect x="20" y="26" width="8" height="7"/><rect x="32" y="26" width="8" height="7"/><rect x="44" y="26" width="8" height="7"/><rect x="56" y="26" width="8" height="7"/>
        <rect x="20" y="40" width="8" height="7"/><rect x="32" y="40" width="8" height="7"/><rect x="44" y="40" width="8" height="7"/><rect x="56" y="40" width="8" height="7"/>
        <rect x="20" y="54" width="8" height="7"/><rect x="32" y="54" width="8" height="7"/><rect x="44" y="54" width="8" height="7"/><rect x="56" y="54" width="8" height="7"/>
        <rect x="20" y="68" width="8" height="7"/><rect x="32" y="68" width="8" height="7"/><rect x="44" y="68" width="8" height="7"/><rect x="56" y="68" width="8" height="7"/>
        <rect x="78" y="40" width="6" height="6"/><rect x="78" y="54" width="6" height="6"/><rect x="78" y="68" width="6" height="6"/>
      </g>
    </svg>
    <div class="service-name">Commercial Building</div>
  </div>

  <div class="service s-concrete">
    <svg viewBox="0 0 130 94" style="width:128px" fill="none" stroke="var(--olive)" stroke-width="4" stroke-linejoin="round">
      <path d="M6 70 V44 L14 30 H34 V70 Z M14 44 H30 V32"/>
      <path d="M34 70 H118 V62 H34"/>
      <path d="M44 58 L52 26 C70 12 96 12 108 20 L112 56 Z"/>
      <path d="M60 22 L66 52 M76 16 L82 54 M92 16 L96 54"/>
      <path d="M110 22 L122 18 L124 30 L114 36"/>
      <circle cx="22" cy="78" r="7"/><circle cx="62" cy="78" r="7"/><circle cx="82" cy="78" r="7"/><circle cx="104" cy="78" r="7"/>
      <path d="M2 90 H128"/>
    </svg>
    <div class="service-name">Concrete</div>
  </div>

  <div class="service s-painting">
    <svg viewBox="0 0 100 94" fill="none" stroke="var(--olive)" stroke-width="4" stroke-linejoin="round">
      <rect x="18" y="6" width="62" height="22" rx="4"/><path d="M26 12 H72"/>
      <path d="M80 17 H88 V40 H50 V54"/>
      <rect x="44" y="54" width="12" height="36" rx="6"/>
    </svg>
    <div class="service-name">Painting</div>
  </div>

  <div class="skyline" role="img" aria-label="Sketched city skyline of glass towers and construction cranes under soft blue clouds, standing on a patch of green grass"></div>

  <footer class="footer">
    <div class="brand"><span class="brand-dot"></span>KESTREL</div>
    <div class="contact">
      <div class="contact-row">
        <span><strong>HOME OFFICE:</strong> 1300 00 4821</span>
        <span class="sep">•</span>
        <span>Suite 2.04, 18 Harbour Lane Parkview</span>
      </div>
      <div class="contact-rule"></div>
      <div class="contact-row cities">
        <span><strong>WWW.KESTREL-SERVICES.COM.AU</strong> SYDNEY | CANBERRA | BRISBANE | MELBOURNE</span>
      </div>
    </div>
  </footer>
</div>
</body>
</html>
```